Willowmere Counseling (Endure - Mend - Flourish) - Double Sided Business Card

I would like a 2-sided business card. Front: Matte Black or Navy with Logo & Tagline. Back: Name, Address, Phone Number, Email, & Website (maybe would like to include a small map pin-pointing location); Prefer front to be a gold/silver foil (iridescent); Back prefer white or light colored background with lettering that is easy to read and simple

Target Market(s)

Individuals & Couples (13 y.o. - ALL Adults); High end clientele

Industry/Entity Type

Licensed Professional Counselor (Mental Health)

Contact Information for Business Card

Name: Willowmere Counseling; Tagline: Endure - Mend - Flourish; Address: 3870 N. Garrick Ave., Suite 214, Fort Worth, TX 76132; Phone: (214) 555-0187; Website: www.WillowmereCounseling.example

Font styles to use
Serif

Requirements
Must have
• Logo on Front (Large) prefer gold/silver foil on a matte dark color (i.e. black, navy, etc.); Back of Card: All other relevant information

```html
<!DOCTYPE html>
<html lang="en">
<head>
<meta charset="utf-8">
<title>Willowmere Counseling – Business Card</title>
<link rel="stylesheet" href="https://fonts.googleapis.com/css2?family=Cinzel:wght@500&family=Cormorant+Garamond:wght@500&family=Arimo:wght@400;700&display=swap">
<style>
  :root {
    --backdrop: #e3e3e3;
    --card-white: #f7f7f6;
    --gold: #d3b862;
    --grey: #8c8c8c;
    --ink: #262626;
    --white: #ffffff;
  }
  * { margin: 0; padding: 0; box-sizing: border-box; }
  html, body { width: 1200px; height: 930px; overflow: hidden; }
  body {
    background: radial-gradient(ellipse at 50% 40%, #efefef 0%, var(--backdrop) 75%);
    position: relative;
  }
  .card {
    position: absolute;
    top: 315px;
    width: 525px;
    height: 300px;
    box-shadow: 0 10px 26px rgba(0,0,0,0.18);
  }

  /* Back of card: contact side */
  .card-back { left: 50px; background: var(--card-white); }
  .brand-row {
    position: absolute; top: 52px; left: 0; right: 0;
    display: flex; align-items: center; justify-content: center; gap: 14px;
  }
  .brand-dot { width: 40px; height: 40px; border-radius: 50%; background: var(--gold); }
  .brand-block { text-align: center; }
  .brand-name {
    font-family: "Cinzel", serif; font-weight: 500;
    font-size: 25px; letter-spacing: 1.5px; color: var(--gold);
    border-bottom: 1.5px solid var(--grey); padding-bottom: 3px;
  }
  .brand-tagline {
    font-family: "Cormorant Garamond", serif; font-weight: 500;
    font-size: 11px; letter-spacing: 1.4px; text-transform: uppercase;
    color: var(--gold); margin-top: 4px;
  }
  .details {
    position: absolute; top: 148px; left: 0; right: 0;
    display: flex; justify-content: center; align-items: center;
  }
  .person { text-align: right; padding-right: 18px; }
  .person-name {
    font-family: "Arimo", sans-serif; font-weight: 700;
    font-size: 15px; letter-spacing: 1px; color: var(--gold); text-transform: uppercase;
  }
  .person-role { font-family: "Arimo", sans-serif; font-size: 12px; color: var(--ink); margin-top: 3px; }
  .divider { width: 1px; height: 58px; background: #b8b8b8; }
  .contact-list { list-style: none; padding-left: 16px; }
  .contact-list li {
    display: flex; align-items: center; gap: 7px;
    font-family: "Arimo", sans-serif; font-size: 12px; color: var(--ink); line-height: 19px;
  }
  .contact-list svg { width: 11px; height: 11px; flex: none; }
  .address {
    position: absolute; bottom: 40px; left: 0; right: 0; text-align: center;
    font-family: "Arimo", sans-serif; font-size: 12.5px; color: var(--ink);
  }

  /* Front of card: brand side */
  .card-front { left: 625px; background: var(--gold); }
  .front-brand {
    position: absolute; inset: 0;
    display: flex; align-items: center; justify-content: center; gap: 16px;
  }
  .front-dot { width: 52px; height: 52px; border-radius: 50%; background: var(--white); }
  .front-brand .brand-name { color: var(--white); font-size: 30px; border-bottom-color: var(--white); }
  .front-brand .brand-tagline { color: var(--white); font-size: 12.5px; }
</style>
</head>
<body>

<section class="card card-back" aria-label="Business card back">
  <div class="brand-row">
    <span class="brand-dot"></span>
    <div class="brand-block">
      <p class="brand-name">Willowmere Counseling</p>
      <p class="brand-tagline">Endure - Mend - Flourish</p>
    </div>
  </div>

  <div class="details">
    <div class="person">
      <p class="person-name">Daniel Hartley</p>
      <p class="person-role">Managing Director</p>
    </div>
    <span class="divider"></span>
    <ul class="contact-list">
      <li>
        <svg viewBox="0 0 24 24" aria-hidden="true"><path fill="#d3b862" d="M6.6 10.8a15.1 15.1 0 0 0 6.6 6.6l2.2-2.2a1 1 0 0 1 1-.25 11.4 11.4 0 0 0 3.6.57 1 1 0 0 1 1 1V20a1 1 0 0 1-1 1A17 17 0 0 1 3 4a1 1 0 0 1 1-1h3.5a1 1 0 0 1 1 1c0 1.25.2 2.45.57 3.57a1 1 0 0 1-.25 1z"/></svg>
        (214) 555-0187
      </li>
      <li>
        <svg viewBox="0 0 24 24" aria-hidden="true"><path fill="#d3b862" d="M2 5h20v14H2z"/><path fill="none" stroke="#fff" stroke-width="2" d="M2 5l10 8 10-8"/></svg>
        info@WillowmereCounseling.example
      </li>
      <li>
        <svg viewBox="0 0 24 24" aria-hidden="true"><circle cx="12" cy="12" r="10" fill="#d3b862"/><path fill="none" stroke="#fff" stroke-width="1.5" d="M2 12h20M12 2c3 3 3 17 0 20M12 2c-3 3-3 17 0 20"/></svg>
        www.WillowmereCounseling.example
      </li>
    </ul>
  </div>

  <p class="address">3870 N. Garrick Ave., Suite 214, Fort Worth, TX 76132</p>
</section>

<section class="card card-front" aria-label="Business card front">
  <div class="front-brand">
    <span class="front-dot"></span>
    <div class="brand-block">
      <p class="brand-name">Willowmere Counseling</p>
      <p class="brand-tagline">Endure - Mend - Flourish</p>
    </div>
  </div>
</section>

</body>
</html>
```